back to back colour flier for child/teen psychology business

a5 size please, full colour.
modern, fresh.
appeals to parents.
with my logo which is attached, as is required text.

Updates
remember that we work with both children and teens, so any images would have to incorporate both groups.  Or have an image of a child as well as a teen........

Industry/Entity Type
Business

```html
<!DOCTYPE html>
<html lang="en">
<head>
<meta charset="utf-8">
<title>Get Help For Your Child – Flyer</title>
<link rel="stylesheet" href="https://fonts.googleapis.com/css2?family=Mulish:ital,wght@0,400;0,600;0,800;1,400&family=Poppins:wght@800&display=swap">
<style>
  :root{
    --canvas:#e9e9e9;
    --paper:#ffffff;
    --ink:#2a1e12;
    --brown:#5a3a1c;
    --sepia-light:#f3ead9;
    --sepia-mid:#c9ad85;
    --sepia-deep:#6e5233;
    --band:#1d1710;
    --green:#5f8f3a;
    --white:#ffffff;
  }
  *{box-sizing:border-box;margin:0;padding:0}
  html,body{width:1200px;height:1000px;overflow:hidden;background:var(--canvas)}
  body{position:relative;font-family:"Mulish",sans-serif;color:var(--ink)}

  .flyer{position:absolute;left:100px;top:146px;width:1000px;height:707px;background:var(--paper);overflow:hidden;box-shadow:0 6px 22px rgba(0,0,0,.18)}

  .hero-photo{position:absolute;left:0;top:0;width:1000px;height:540px;
    background:
      radial-gradient(ellipse 230px 300px at 850px 300px, #8a6a45 0%, rgba(138,106,69,.6) 45%, rgba(138,106,69,0) 75%),
      linear-gradient(180deg, var(--sepia-light) 0%, #e6d6b8 35%, var(--sepia-mid) 65%, var(--sepia-deep) 100%);}
  .hero-fade{position:absolute;left:0;top:0;width:700px;height:540px;
    background:linear-gradient(90deg, rgba(250,245,235,.85) 0%, rgba(250,245,235,.55) 60%, rgba(250,245,235,0) 100%)}

  .headline{position:absolute;left:38px;top:26px;font-family:"Poppins",sans-serif;font-weight:800;font-size:50px;letter-spacing:1px;color:var(--brown);text-transform:uppercase;
    text-shadow:-2px -2px 0 var(--white),2px 2px 0 var(--white),2px -2px 0 var(--white),-2px 2px 0 var(--white)}

  .copy{position:absolute;left:40px;top:98px;width:620px;font-size:13.5px;line-height:1.35;color:var(--ink)}
  .copy .intro{font-style:italic;font-size:12.5px;margin-bottom:2px}
  .concerns{list-style:none;font-weight:800;font-size:15px;line-height:1.3;margin-bottom:8px}
  .copy p{margin-bottom:5px}

  .offices-band{position:absolute;left:0;top:420px;width:660px;height:86px}
  .offices-text{position:absolute;left:40px;top:436px;width:570px;color:var(--white);font-weight:800;font-size:17px;line-height:1.35}

  .contact{position:absolute;left:40px;top:552px;width:420px}
  .contact .lead{color:var(--green);font-size:20px;font-weight:600}
  .contact .phone{font-family:"Poppins",sans-serif;font-weight:800;font-size:50px;color:var(--brown);line-height:1.05;letter-spacing:2px}
  .contact .note{font-size:12.5px;font-weight:600;color:var(--ink);line-height:1.35;margin-top:4px}

  .brand{position:absolute;left:560px;top:575px;width:400px;display:flex;align-items:center;gap:14px}
  .brand .mark{width:30px;height:30px;border-radius:50%;background:var(--green);flex:none}
  .brand .name{font-weight:800;font-size:24px;line-height:1.2;color:var(--green);text-transform:uppercase}
</style>
</head>
<body>
  <main class="flyer">
    <div class="hero-photo" role="img" aria-label="Sepia photograph of a young child sitting on the grass hugging their knees, head down"></div>
    <div class="hero-fade"></div>

    <h1 class="headline">Get Help For Your Child</h1>

    <section class="copy">
      <p class="intro">Many children and teens have times in life when they:</p>
      <ul class="concerns">
        <li>Feel worried, panicky and stressed</li>
        <li>Have trouble managing their frustration</li>
        <li>Struggle with friendships and getting along with others</li>
        <li>Feel down, sad or hopeless</li>
        <li>Find school hard, or struggle to motivate themselves</li>
      </ul>
      <p>If you know or have a child/teen in this situation, then we can help. At Growing Pathways Psychology and Education, we have eight experienced clinical psychologists who only work with children and teens and have worked with families in all kinds of situations.</p>
      <p>We work with children/teens to build their resiliency, feel more positive, cope constructively with frustration and learn to get along with families and friends.</p>
      <p>We work with parents to help them know how to respond to and support the young person during this time.</p>
      <p>The majority of the cost of consultations are usually covered by HealthCover.</p>
    </section>

    <svg class="offices-band" viewBox="0 0 660 86" aria-hidden="true">
      <polygon points="0,0 660,0 610,86 0,86" fill="var(--band)"/>
    </svg>
    <p class="offices-text">We have child and teen friendly offices at Hillcrest Park and Riverton, and have some after school hours consultations.</p>

    <section class="contact">
      <p class="lead">For more information call</p>
      <p class="phone">8042 5519</p>
      <p class="note">or you can visit our website and also read a range of free articles about helping kids and young people through tough times.</p>
    </section>

    <section class="brand">
      <span class="mark"></span>
      <p class="name">Growing Pathways Psychology and Education</p>
    </section>
  </main>
</body>
</html>
```